LANDING PAGE DESIGN - MONEY GUARANTEED & 2ND PLACE PAYOUT

taskporch42.com
Top Slide
Are you interested in earning from $65,000.00 - $91,000.00 a year from home?
NO PREVIOUS MARKETING EXPERIENCE NEEDED
---- scene 2 of slide --- please provide nice graphical images along with the text on each slide --
We are looking for motivated individuals from “GEO IP” with to join our team.
Qualify below to earn $100.00 a day while u learn to make $$
---Please don’t forget to create both slides when u post your design ---
Who should apply?
Anyone from the age of 18-65 who has at least 6 months experience using Pixelnook and or Tradeboard. There is no marketing experience necessary or required and no background checks will be ran. The only really requirements are a home computer and internet connection and the ability to follow simple directions.

__featured jobs section__ Please make this section feature the 2 current available positions we are hiring for
Available Positions – Pixelnook AD Specialist –
Enroll in an 8 week training class that pays you $500.00 per week.
Training takes about 30-60 minutes a day 5 days a week for 8 weeks. Make $100.00 a day during training, and $250.00 a day 5-7 days a week after training is complete.
What do we do?
Help small businesses sale products through social media channels like Pixelnook & Snapverge. Our customers primary focus on the health and beauty niche.
Tradeboard Post Specialist
Enroll in a 6 weeks training that pays you $25.00 per day. Earn $100.00 a day after successfully completing your training. Course requires 30 minutes per day at least 3 times per week.
What do we do?
We help local real estate brokers, insurance agents, and other small businesses grow their businesses through targeted classified ad posting all over the country.

How do you apply?

First you must fill out our short application.
(Create an iframe - Frame #1)
First Name, Last Name, Age, City, State, Zip, Phone, Email
(Frame #2)
Do you have a desktop or laptop computer?
Do you have 24/7 access to the internet?
Are you at least 18 years old?
Do you have Photo ID? (must match your Pixelnook name)
Are you ready to start making money immediately?
(end of frames)

Testimonials Section
Leave space/frame for 3 video testimonials

Get Paid Referring Friends (need someway to track / pay for referrals)
We will pay you $5.00 for every qualified friend that you refer to us. Fill out the application above to get more information on our referral program.

After they complete the application I would like them to be sent an email saying that they qualify for both positions but we don’t have training agents available until “random day 2-3 months ahead”
BUT YOU QUALIFY FOR OUR SECONDARY OFFER
Would you like to earn $100.00 today – and up to $150.00 a week while getting a jump start on your training? “they click yes or no” when they click yes – it would take them to another page which explains to them to download TeamViewer so we can run ads from their PN promoting our partners and we will pay them weekly for it.

Target Market(s)

Lower Income Users Looking to make $$ from home who have an active Pixelnook account as well as a home computer and high speed internet.

Industry/Entity Type

Marketing

Number of Pages Required

1 page

Requirements
Must have
• This is a landing page / lead capturing page - So please make sure that the site focuses on pushing the user to enter their contact details and submit our qualifier form.
Nice to have
• I've always like the more cartoony websites - but must still be clean/professional looking with proper use of the fold of the page and whitespaces.

```html
<!DOCTYPE html>
<html lang="en">
<head>
<meta charset="utf-8">
<title>Taskporch Requirements – Work From Home</title>
<link href="https://fonts.googleapis.com/css2?family=Open+Sans:wght@400;600;700;800&family=Raleway:wght@400;600;700&display=swap" rel="stylesheet">
<style>
:root{
  --blue:#1a86cc;
  --blue-dark:#0f5f99;
  --navy:#0b3f69;
  --ink:#2b2b2b;
  --muted:#666;
  --charcoal:#3b3d40;
  --charcoal-dark:#2c2e31;
  --light:#f3f5f7;
  --line:#d9dde1;
  --white:#fff;
}
*{box-sizing:border-box;margin:0;padding:0}
html,body{width:1200px;height:2636px;overflow:hidden}
body{font-family:"Open Sans",Arial,sans-serif;color:var(--ink);background:var(--white)}
.page{width:1200px;height:2636px;position:relative}

/* header */
.site-header{height:116px;display:flex;align-items:center;justify-content:space-between;padding:0 60px 0 68px;background:var(--white)}
.brand{display:flex;align-items:center;gap:12px}
.brand-dot{width:38px;height:38px;border-radius:50%;background:var(--blue)}
.brand-name{font-size:30px;font-weight:700;color:var(--navy);line-height:1}
.brand-name small{display:block;font-size:14px;font-weight:700;letter-spacing:1px;margin-top:4px;color:var(--navy)}
.header-actions{display:flex;flex-direction:column;align-items:flex-end;gap:10px}
.header-buttons{display:flex;gap:8px}
.btn{display:inline-block;border:0;font-family:inherit;font-weight:700;text-transform:uppercase;letter-spacing:.5px;color:var(--white)}
.btn-small{font-size:12px;padding:8px 18px;background:var(--charcoal-dark)}
.btn-small.blue{background:var(--blue)}
.header-call{font-size:15px;color:var(--muted)}
.header-call strong{color:var(--blue);font-weight:700}

/* hero */
.hero{height:444px;position:relative;background:linear-gradient(135deg,#1f93d8,#116aad);overflow:hidden}
.hero-copy{position:absolute;left:128px;top:84px;width:520px;color:var(--white)}
.hero-copy h1{font-size:33px;font-weight:600;line-height:1.3}
.hero-copy h2{font-size:22px;font-weight:700;margin-top:14px}
.hero-copy .btn{margin-top:26px;font-size:14px;padding:12px 28px;background:var(--charcoal-dark)}
.hero-art{position:absolute;right:70px;top:28px;width:420px;height:390px;border-radius:8px;background:linear-gradient(160deg,#4fb3ea,#1b78bb)}
.hero-arrow{position:absolute;top:200px;width:30px;height:30px}
.hero-arrow.left{left:30px}.hero-arrow.right{right:30px}

/* who should apply */
.who{height:380px;position:relative;background:var(--white)}
.who-art{position:absolute;left:70px;top:70px;width:220px;height:230px;border-radius:8px;background:linear-gradient(160deg,#f2c9a9,#c97d52)}
.section-title{font-family:"Raleway","Open Sans",sans-serif;font-weight:400;font-size:40px;color:var(--ink)}
.section-title em{font-style:normal;color:var(--blue);font-weight:600}
.who .section-title{position:absolute;left:330px;top:94px}
.who-rule{position:absolute;left:330px;top:158px;width:60px;height:3px;background:var(--blue)}
.who p{position:absolute;left:330px;top:176px;width:800px;font-size:15px;line-height:1.7;color:var(--muted)}

/* featured jobs */
.jobs{height:572px;position:relative;background:linear-gradient(180deg,var(--charcoal),var(--charcoal-dark));color:var(--white)}
.jobs .section-title{color:var(--white);text-align:center;padding-top:30px}
.jobs-rule{width:60px;height:3px;background:var(--blue);margin:14px auto 0}
.job{position:absolute;top:150px;width:300px;font-size:12.5px;line-height:1.6;color:#cfd3d7}
.job h3{font-size:18px;font-weight:700;color:var(--white);margin-bottom:10px}
.job h4{font-size:15px;font-weight:700;color:var(--white);margin:18px 0 6px}
.job strong{color:var(--white)}
.job.left{left:90px;text-align:right}
.job.right{left:830px}
.job-icon{position:absolute;top:152px;width:56px;height:56px;border-radius:50%;background:var(--blue)}
.job-icon.left{left:412px}.job-icon.right{left:738px}
.jobs-art{position:absolute;left:480px;top:130px;width:240px;height:290px;border-radius:8px;background:linear-gradient(180deg,#5a5d61,#44474b)}
.jobs .btn{position:absolute;left:470px;top:470px;width:260px;text-align:center;font-size:13px;padding:13px 0;background:var(--blue)}

/* apply form */
.apply{height:388px;position:relative;background:var(--light)}
.apply .section-title{text-align:center;padding-top:24px;font-size:38px}
.apply-sub{text-align:center;font-size:14px;color:var(--muted);margin-top:6px}
.form-grid{position:absolute;left:280px;top:114px;width:640px;display:grid;grid-template-columns:1fr 1fr;gap:8px 24px}
.field{height:30px;background:var(--white);border:1px solid var(--line);font-size:12px;color:#999;padding:6px 12px}
.apply .btn{position:absolute;left:538px;top:272px;width:124px;text-align:center;font-size:12px;padding:9px 0;background:var(--blue)}
.checks{position:absolute;left:200px;top:308px;width:800px;display:grid;grid-template-columns:1fr 1fr;gap:5px 40px;font-size:12.5px;line-height:1.4;color:var(--muted)}
.check{display:flex;align-items:center;gap:8px}
.check i{width:13px;height:13px;border:1px solid #aab;background:var(--white);flex:none}

/* referral */
.referral{height:300px;position:relative;background:linear-gradient(135deg,#1d8fd4,#1470b2);color:var(--white)}
.referral-art{position:absolute;left:70px;top:50px;width:190px;height:210px;border-radius:8px;background:linear-gradient(160deg,#7cc6ef,#2b84c2)}
.referral-copy{position:absolute;left:290px;top:70px;width:860px}
.referral h2{font-size:21px;font-weight:700;line-height:1.3;white-space:nowrap}
.referral p{margin-top:16px;width:720px;font-size:15px;line-height:1.7;color:#e5f2fb}

/* testimonials */
.testimonials{height:400px;position:relative;background:var(--white)}
.testimonials .section-title{text-align:center;padding-top:22px;font-size:38px}
.cards{position:absolute;left:150px;top:104px;width:900px;display:grid;grid-template-columns:repeat(3,1fr);gap:30px}
.card{position:relative;height:250px;background:linear-gradient(160deg,#c9cdd2,#8e959c);box-shadow:0 2px 8px rgba(0,0,0,.18)}
.card:nth-child(2){background:linear-gradient(160deg,#d8c3ad,#8f7357)}
.card:nth-child(3){background:linear-gradient(160deg,#b9c3cc,#6f7d88)}
.play{position:absolute;left:50%;top:42%;width:50px;height:50px;margin:-25px 0 0 -25px}
.card-caption{position:absolute;left:0;right:0;bottom:0;padding:10px 16px;background:rgba(0,0,0,.55);color:var(--white);font-size:13px;font-weight:600}

/* footer */
.site-footer{height:36px;background:var(--navy);color:#c6d6e4;font-size:12px;display:flex;align-items:center;justify-content:center}
</style>
</head>
<body>
<div class="page">

  <header class="site-header">
    <div class="brand">
      <span class="brand-dot"></span>
      <div class="brand-name">taskporch<small>REQUIREMENTS</small></div>
    </div>
    <div class="header-actions">
      <div class="header-buttons">
        <span class="btn btn-small">Apply Now</span>
        <span class="btn btn-small blue">Login</span>
      </div>
      <div class="header-call">Have a question? Call us Now <strong>555 019 2847</strong></div>
    </div>
  </header>

  <section class="hero">
    <svg class="hero-arrow left" viewBox="0 0 30 30"><path d="M20 4 9 15l11 11" fill="none" stroke="#fff" stroke-width="3"/></svg>
    <div class="hero-copy">
      <h1>Are You Interested In Earning From $65,000.00 - $91,000.00 A Year From Home?</h1>
      <h2>No Previous Marketing Experience Needed</h2>
      <span class="btn">Apply Now</span>
    </div>
    <div class="hero-art" role="img" aria-label="Illustration of a man working at a desk with a large computer monitor"></div>
    <svg class="hero-arrow right" viewBox="0 0 30 30"><path d="M10 4l11 11-11 11" fill="none" stroke="#fff" stroke-width="3"/></svg>
  </section>

  <section class="who">
    <div class="who-art" role="img" aria-label="Illustration of two women sitting at a home computer"></div>
    <h2 class="section-title">Who <em>should apply</em></h2>
    <div class="who-rule"></div>
    <p>Anyone from the age of 18-65 who has at least 6 months experience using Pixelnook and or Tradeboard. There is no marketing experience necessary or required and no background checks will be ran. The only really requirements are a home computer and internet connection and the ability to follow simple directions.</p>
  </section>

  <section class="jobs">
    <h2 class="section-title">Featured Jobs</h2>
    <div class="jobs-rule"></div>

    <div class="job left">
      <h3>Pixelnook AD Specialist</h3>
      <p>Enroll in an <strong>8 week</strong> training class that pays you <strong>$500.00</strong> per week.</p>
      <p style="margin-top:10px">Training takes about 30-60 minutes a day 5 days a week for 8 weeks. Make $100.00 a day during training, and $250.00 a day 5-7 days a week after training is complete.</p>
      <h4>What do we do?</h4>
      <p>Help small businesses sale products through social media channels like Pixelnook &amp; Snapverge. Our customers primary focus on the health and beauty niche.</p>
    </div>
    <span class="job-icon left"></span>

    <div class="jobs-art" role="img" aria-label="Illustration of a person standing behind a desk presenting both positions"></div>

    <span class="job-icon right"></span>
    <div class="job right">
      <h3>Tradeboard Post Specialist</h3>
      <p>Enroll in a <strong>6 weeks</strong> training that pays you <strong>$25.00</strong> per day.</p>
      <p style="margin-top:10px">Earn $100.00 a day after successfully completing your training. Course requires 30 minutes per day at least 3 times per week.</p>
      <h4>What do we do?</h4>
      <p>We help local real estate brokers, insurance agents, and other small businesses grow their businesses through targeted classified ad posting all over the country.</p>
    </div>

    <span class="btn">Frequently Asked Questions</span>
  </section>

  <section class="apply">
    <h2 class="section-title">Apply <em>Here To Qualify</em></h2>
    <p class="apply-sub">First you must fill out our short application.</p>
    <div class="form-grid">
      <div class="field">First Name</div><div class="field">Last Name</div>
      <div class="field">Age</div><div class="field">City</div>
      <div class="field">State</div><div class="field">Zip</div>
      <div class="field">Phone</div><div class="field">Email</div>
    </div>
    <span class="btn">Submit Now</span>
    <div class="checks">
      <div class="check"><i></i>Do you have a desktop or laptop computer?</div>
      <div class="check"><i></i>Do you have Photo ID? (must match your Pixelnook name)</div>
      <div class="check"><i></i>Do you have 24/7 access to the internet?</div>
      <div class="check"><i></i>Are you at least 18 years old?</div>
      <div class="check"><i></i>Are you ready to start making money immediately?</div>
    </div>
  </section>

  <section class="referral">
    <div class="referral-art" role="img" aria-label="Illustration of a group of friends being referred"></div>
    <div class="referral-copy">
      <h2>Get Paid Referring Friends (need someway to track / pay for referrals)</h2>
      <p>We will pay you <strong>$5.00</strong> for every qualified friend that you refer to us. Fill out the application above to get more information on our referral program.</p>
    </div>
  </section>

  <section class="testimonials">
    <h2 class="section-title">What People <em>Are Saying</em></h2>
    <div class="cards">
      <div class="card" role="img" aria-label="Video testimonial from a member">
        <svg class="play" viewBox="0 0 50 50"><circle cx="25" cy="25" r="24" fill="rgba(0,0,0,.45)"/><path d="M20 15v20l16-10z" fill="#fff"/></svg>
        <div class="card-caption">Member story one</div>
      </div>
      <div class="card" role="img" aria-label="Video testimonial from a member">
        <svg class="play" viewBox="0 0 50 50"><circle cx="25" cy="25" r="24" fill="rgba(0,0,0,.45)"/><path d="M20 15v20l16-10z" fill="#fff"/></svg>
        <div class="card-caption">Member story two</div>
      </div>
      <div class="card" role="img" aria-label="Video testimonial from a member">
        <svg class="play" viewBox="0 0 50 50"><circle cx="25" cy="25" r="24" fill="rgba(0,0,0,.45)"/><path d="M20 15v20l16-10z" fill="#fff"/></svg>
        <div class="card-caption">Member story three</div>
      </div>
    </div>
  </section>

  <footer class="site-footer">Copyright ©2017 Taskporch42 All Rights Reserved</footer>

</div>
</body>
</html>
```